依頼詳細
STUDIOを使用して、LP制作をお願いいたします。

◆LPの目的
エンジニア向けオンライン採用イベントの参加者募集
対象はリモートワークを希望するエンジニアが中心となります。
閲覧する年齢層については20~40歳前後を想定しております。

◆構成
LPのみとなりますが、
CTAとして、SlotBookというツールのカレンダーをiframeで埋め込む形となりますので、埋め込み可能なエリアを用意したうえでご提案ください。

詳細は各セクションのコピーのファイルに記載しております。

◆納品方法
①STUDIOでプロジェクトを立ち上げて制作し、プレビュー画面のURLをご共有ください。
②選定後、弊社のアカウントをプロジェクトに招待していただき、権限を弊社に移行してください。
③権限移行の確認後、選定完了およびお支払いを致します。

◆補足
選定後、広告運用の効果を高めるために修正のご依頼を別途継続の案件としてご依頼する場合があります。

◆参考イメージサイト
https://jobs.tarnivo.com/about/scout
https://kzmq.jp/archives/otherdesign/lp/73832
https://kzmq.jp/archives/otherdesign/lp/73820
https://kzmq.jp/archives/otherdesign/lp/99010
サイトURL
https://web-plumoria.com/
ページ数
1ページ
希望イメージ
シンプル 複雑
単色 カラフル
暗い 明るい
日常 高級
遊び心 厳粛
未来的 伝統的
女性的 男性的
希望する色
青系
■ 選んだ理由

パッと見た際のデザインの印象が最もイメージに近く、
また納品を前提とした細かな修正にもご対応をいただけました。

かなりご無理を申し上げてしまったなか、
誠にありがとうございました!

■ 提案者全員のお礼・コメント

その他、ご提案頂いた方もありがとうございました。
また募集の機会がありましたら、ぜひまたよろしくお願い申し上げます。

```html
<!DOCTYPE html>
<html lang="ja">
<head>
<meta charset="UTF-8">
<title>オンライン ソラノ転職EXPO</title>
<link rel="stylesheet" href="https://fonts.googleapis.com/css2?family=Noto+Sans+JP:wght@400;500;700;900&family=Montserrat:wght@500;700;800&display=swap">
<style>
:root{
  --blue:#1a73e8;
  --blue-deep:#0d47a1;
  --blue-light:#e8f1fd;
  --blue-pale:#f3f7fc;
  --navy:#0a1e45;
  --ink:#1b2430;
  --grey:#6b7380;
  --line:#d9e1ec;
  --white:#ffffff;
  --red:#e53935;
}
*{box-sizing:border-box;margin:0;padding:0}
html,body{width:1200px;height:4992px;overflow:hidden}
body{font-family:"Noto Sans JP",sans-serif;color:var(--ink);background:var(--white)}
.en{font-family:"Montserrat",sans-serif}
section,header,footer{position:relative;width:1200px;overflow:hidden}
.btn{display:inline-flex;align-items:center;justify-content:center;background:var(--blue);color:var(--white);font-weight:700;border-radius:999px;font-size:15px;height:48px;padding:0 32px;box-shadow:0 6px 14px rgba(26,115,232,.25);white-space:nowrap}
.label{font-family:"Montserrat",sans-serif;color:var(--blue);font-weight:700;font-size:15px;text-align:center}
.heading{font-size:34px;font-weight:900;text-align:center;margin-top:6px;letter-spacing:.04em}
.lead{font-size:14px;color:var(--grey);text-align:center;margin-top:14px;line-height:1.9}
.placeholder{border-radius:12px}

/* header */
.site-header{height:72px;display:flex;align-items:center;padding:0 32px;background:var(--white);box-shadow:0 1px 0 var(--line)}
.site-header .brand{font-size:22px;font-weight:700;color:var(--blue)}
.site-header nav{margin-left:auto;display:flex;gap:28px;font-size:14px;font-weight:500;align-items:center}
.site-header .btn{height:40px;font-size:13px;padding:0 24px;margin-left:12px}

/* hero */
.hero{height:588px;background:linear-gradient(180deg,#f6f9fe,#eaf2fc)}
.hero .art{position:absolute;left:0;top:0;width:560px;height:520px;background:linear-gradient(135deg,#cfe2fb 0%,#5a9cf0 55%,#1a73e8 100%);border-radius:0 0 180px 0;opacity:.85}
.hero .copy{position:absolute;left:600px;top:44px}
.hero .tag{display:inline-block;background:var(--blue);color:var(--white);font-weight:700;font-size:17px;padding:10px 22px}
.hero h1{font-size:58px;font-weight:900;line-height:1.25;margin-top:24px;letter-spacing:.02em}
.hero .date{font-family:"Montserrat",sans-serif;color:var(--blue);font-weight:700;font-size:28px;margin-top:14px}
.hero .btn{margin-top:40px;height:60px;width:300px;font-size:17px}
.hero .badge{position:absolute;left:24px;top:540px;background:var(--white);font-size:11px;padding:6px 12px;border-radius:4px;color:var(--grey)}

/* about */
.about{height:500px;background:var(--blue-pale);padding-top:60px}
.about .lead{color:var(--ink)}
.logos{position:absolute;top:260px;left:60px;right:60px;display:flex;gap:22px;justify-content:center;align-items:center}
.logos .logo{width:190px;height:76px;background:var(--white);border:1px solid var(--line);display:flex;align-items:center;justify-content:center;font-weight:700;font-size:18px;color:var(--ink);gap:8px}
.logos .logo i{width:14px;height:14px;background:var(--blue);display:inline-block}
.logos .arrow{width:28px;height:28px;color:var(--blue)}
.about .ghost{position:absolute;top:380px;left:0;right:0;text-align:center;font-family:"Montserrat",sans-serif;font-weight:800;font-size:78px;color:#dce8f8;white-space:nowrap}

/* features */
.features{height:720px;padding-top:56px}
.cards{position:absolute;top:180px;left:32px;right:32px;display:flex;gap:30px}
.card{width:358px;background:var(--white);border:1px solid var(--line);border-radius:8px;padding:20px;box-shadow:0 8px 24px rgba(20,60,120,.08)}
.card:nth-child(2){margin-top:40px}
.card .placeholder{height:250px;background:linear-gradient(160deg,#eef4fd,#b9d4f7)}
.card h3{color:var(--blue);font-size:19px;font-weight:700;text-align:center;margin-top:22px;line-height:1.5}
.card p{font-size:13px;color:var(--grey);line-height:1.8;margin-top:12px;text-align:center}

/* flow */
.flow{height:560px;background:linear-gradient(180deg,#f1f4f8,#e6ebf1)}
.flow .copy{position:absolute;left:80px;top:110px;width:440px}
.flow .label,.flow .heading{text-align:left}
.flow .lead{text-align:left;color:var(--ink)}
.flow .btn{margin-top:36px}
.flow .placeholder{position:absolute;left:560px;top:70px;width:560px;height:420px;background:linear-gradient(135deg,#dfe8f3,#9fc0ea)}
.flow .chip{position:absolute;background:var(--blue);color:var(--white);font-size:13px;font-weight:700;padding:10px 18px;border-radius:4px;white-space:nowrap}

/* schedule */
.schedule{height:1080px;padding-top:50px}
.session{position:absolute;left:240px;top:200px;width:720px;border:1px solid var(--line);border-radius:6px;overflow:hidden;box-shadow:0 8px 24px rgba(20,60,120,.08)}
.session .head{background:var(--blue);color:var(--white);font-size:22px;font-weight:700;text-align:center;padding:14px}
.session .body{padding:26px;text-align:center}
.session .when{font-size:17px;font-weight:700}
.session .note{font-size:12px;color:var(--grey);margin-top:8px}
.session .note.red{color:var(--red)}
.session .btn{margin-top:22px}
.timeline{position:absolute;top:500px;left:20px;right:20px;display:flex;gap:40px}
.step{width:360px;height:380px;background:var(--blue-pale);border:1px solid var(--line);border-radius:6px;padding:22px}
.step .pill{display:inline-block;background:var(--blue);color:var(--white);font-weight:700;font-size:15px;padding:8px 20px;border-radius:4px}
.step p{font-size:13px;color:var(--ink);margin-top:16px;line-height:1.8}
.step .btn{height:42px;font-size:13px;margin-top:20px;border-radius:4px}
.step .link{color:var(--blue);text-decoration:underline;font-size:13px;margin-top:14px;line-height:1.7}
.step .placeholder{height:130px;margin-top:16px;background:linear-gradient(160deg,#eef4fd,#b9d4f7)}
.step.split{background:none;border:none;padding:0;display:flex;flex-direction:column;gap:20px}
.step.split .box{flex:1;background:var(--white);border:1px solid var(--line);border-radius:6px;padding:22px}
.step.split h4{font-size:17px;font-weight:700}
.step.split .box p{margin-top:10px}
.step.split .red{color:var(--red)}
.months{position:absolute;top:900px;left:0;width:1200px;height:44px}
.month-labels{position:absolute;top:956px;left:0;width:1200px;display:flex;font-size:22px;font-weight:700;color:var(--blue)}
.month-labels span{width:400px;text-align:center}
.down{position:absolute;top:990px;left:540px}

/* entry */
.entry{height:1120px;background:linear-gradient(180deg,#0a1e45,#123a80 60%,#1a5fc4);color:var(--white);padding-top:70px}
.entry .label{color:#8fbaf7}
.entry .heading{font-size:42px}
.entry .lead{color:#d7e4f8}
.calendar{position:absolute;left:100px;top:270px;width:1000px;height:760px;background:var(--white);border-radius:6px;color:var(--ink);overflow:hidden}
.cal-top{height:64px;border-bottom:1px solid var(--line);display:flex;align-items:center;padding:0 24px;font-size:14px}
.cal-top .name{font-weight:700}
.cal-top .month{margin:0 auto;font-size:18px;font-weight:500}
.cal-days{display:flex;padding:24px 24px 0}
.cal-days .day{flex:1;text-align:center}
.cal-days .day b{display:block;font-family:"Montserrat",sans-serif;font-size:44px;font-weight:700;color:#c5ccd6}
.cal-days .day span{font-size:12px;color:#aab2bd}
.cal-days .day.active b{color:var(--ink)}
.cal-days .day.active span{color:var(--ink)}
.slots{display:flex;flex-direction:column;gap:12px;margin-top:18px;align-items:center}
.slots span{width:100px;border:1px solid var(--line);border-radius:4px;padding:10px 0;text-align:center;font-size:14px;font-family:"Montserrat",sans-serif}
.cal-foot{position:absolute;bottom:20px;left:0;right:0;text-align:center;font-size:11px;color:#aab2bd}

/* band & footer */
.band{height:140px;background:linear-gradient(90deg,#1a73e8,#3b8ef0);color:var(--white);display:flex;align-items:center;justify-content:center;font-size:24px;font-weight:700;letter-spacing:.05em}
.site-footer{height:180px;text-align:center;padding-top:40px}
.site-footer .brand{font-size:26px;font-weight:700;color:var(--blue);letter-spacing:.08em}
.site-footer p{font-size:13px;color:var(--grey);margin-top:10px;line-height:1.7}
.copyright{height:32px;background:var(--blue-deep);color:#cfe0fa;font-size:11px;display:flex;align-items:center;justify-content:center}
</style>
</head>
<body>

<header class="site-header">
  <div class="brand">ソラノ転職EXPO</div>
  <nav>
    <span>ソラノ転職EXPOとは？</span>
    <span>メリットと特徴</span>
    <span>イベントの流れ</span>
    <span>スケジュール</span>
    <span class="btn">エントリー（1分で完了）</span>
  </nav>
</header>

<section class="hero">
  <div class="art placeholder" role="img" aria-label="青い立方体が浮かぶ抽象的なイラスト"></div>
  <div class="copy">
    <span class="tag">リモートワークしたいエンジニア限定！</span>
    <h1>オンライン<br>ソラノ転職EXPO</h1>
    <p class="date">2022.10.8(Sat)/9(Sun) 13:00-19:00</p>
    <span class="btn">説明会に応募（1分で完了）</span>
  </div>
  <span class="badge en">Sorano Job EXPO</span>
</section>

<section class="about">
  <p class="label">Sorano Jobchange Expo</p>
  <h2 class="heading">ソラノ転職EXPOとは？</h2>
  <p class="lead">希望条件や経歴を登録するだけで、さまざまな企業からオンラインであなたに直接面談オファーが来る、<br>希望に合う企業と1対1で面談可能なオンライン転職イベントです。</p>
  <div class="logos">
    <svg class="arrow" viewBox="0 0 24 24"><path d="M15 5l-7 7 7 7" fill="none" stroke="currentColor" stroke-width="2.5"/></svg>
    <div class="logo"><i></i>Lumora</div>
    <div class="logo">Kestrel</div>
    <div class="logo">Norvane</div>
    <div class="logo">Hoshiba</div>
    <div class="logo">Tellapoint</div>
    <svg class="arrow" viewBox="0 0 24 24"><path d="M9 5l7 7-7 7" fill="none" stroke="currentColor" stroke-width="2.5"/></svg>
  </div>
  <div class="ghost">Sorano Jobchange Expo</div>
</section>

<section class="features">
  <p class="label">Features</p>
  <h2 class="heading">メリットと特徴</h2>
  <p class="lead">「希望の評価」が「手軽に」見つかる。</p>
  <div class="cards">
    <article class="card">
      <div class="placeholder" role="img" aria-label="自宅のデスクでパソコン作業をする人物のイラスト"></div>
      <h3>リモートワークOKの<br>200社以上が参加</h3>
      <p>「リモートOK」の企業を中心に多数が参加。<br>さらに業種や職種別に探せるから<br>希望に近い企業と出会えます。</p>
    </article>
    <article class="card">
      <div class="placeholder" role="img" aria-label="スマートフォンで登録する人物のイラスト"></div>
      <h3>5分で登録、後は待つだけ<br>手軽に面談</h3>
      <p>経歴や希望条件を登録するだけで<br>企業からオファーが届きます。<br>面談はすべてオンラインで完結。</p>
    </article>
    <article class="card">
      <div class="placeholder" role="img" aria-label="ギフトカードと封筒のイラスト"></div>
      <h3>参加するだけで<br>3,000円のギフト券</h3>
      <p>説明会・面談を1回以上受けた方全員に<br>3,000円分のギフト券をプレゼント。<br>詳細は当日ご案内します。</p>
    </article>
  </div>
</section>

<section class="flow">
  <div class="copy">
    <p class="label">Flow</p>
    <h2 class="heading">イベントの流れ</h2>
    <p class="lead">企業からのチャットや面談依頼を専用ページから確認、<br>面談や面談リクエストへの対応を行います。</p>
    <span class="btn">説明会に応募（1分で完了）</span>
  </div>
  <div class="placeholder" role="img" aria-label="ノートパソコンのビデオ面談画面とスマートフォンのチャット画面"></div>
  <span class="chip" style="left:700px;top:430px">ビデオ通話で面談</span>
  <span class="chip" style="left:900px;top:470px">チャットで面接日程を調整</span>
</section>

<section class="schedule">
  <p class="label">Schedule</p>
  <h2 class="heading">スケジュール</h2>
  <div class="session">
    <div class="head">説明会</div>
    <div class="body">
      <p class="when">第1回 9月2日(金)19:00 ｜ 9月3日(土) 10:00</p>
      <p class="note">所要時間は約30分、オンラインで開催します</p>
      <p class="note red">説明会への参加がエントリーの条件となります</p>
      <p class="note">ご参加にはカレンダーから日時をご予約ください。</p>
      <span class="btn">説明会に応募（1分で完了）</span>
    </div>
  </div>
  <div class="timeline">
    <div class="step">
      <span class="pill">お申込み受付</span>
      <p>登録フォームから経歴情報を<br>お申込みください。</p>
      <span class="btn">エントリー（1分で完了）</span>
      <p class="link">お申込み後の流れを確認<br>参加に関するよくある質問はこちら</p>
    </div>
    <div class="step">
      <span class="pill">イベント当日</span>
      <p>専用ページで企業からのオファーを確認し、<br>面談URLからオンラインで参加します。</p>
      <div class="placeholder" role="img" aria-label="オンライン面談をする人物のイラスト"></div>
    </div>
    <div class="step split">
      <div class="box">
        <h4>雇用成立</h4>
        <p>企業との面談を経て内定となった場合、<br>入社日などを個別に調整します。</p>
      </div>
      <div class="box">
        <h4>雇用なし｜不成立</h4>
        <p class="red">再度イベントにご参加いただけます。<br>安心してご参加ください。</p>
      </div>
    </div>
  </div>
  <svg class="months" viewBox="0 0 1200 44" preserveAspectRatio="none">
    <path d="M0 0H380L400 22 380 44H0Z" fill="#1a73e8"/>
    <path d="M404 0H780L800 22 780 44H404L424 22Z" fill="#1a73e8"/>
    <path d="M804 0H1180L1200 22 1180 44H804L824 22Z" fill="#1a73e8"/>
  </svg>
  <div class="month-labels"><span>9月</span><span>10月</span><span>11月〜</span></div>
  <svg class="down" width="120" height="90" viewBox="0 0 120 90"><path d="M35 0H85V40H120L60 90 0 40H35Z" fill="#9cc2f5"/></svg>
</section>

<section class="entry">
  <p class="label">Entry</p>
  <h2 class="heading">30秒でエントリー完了！</h2>
  <p class="lead">カレンダーからすぐ参加予約を。<br>キャンセルや日程変更もこちらから、いつでもご確認いただけます。</p>
  <div class="calendar">
    <div class="cal-top"><span class="name">Plumo</span><span class="month">10月 2022</span><span>‹ ›</span></div>
    <div class="cal-days">
      <div class="day"><b>09</b><span>日</span></div>
      <div class="day"><b>10</b><span>月</span></div>
      <div class="day"><b>11</b><span>火</span></div>
      <div class="day"><b>12</b><span>水</span></div>
      <div class="day"><b>13</b><span>木</span></div>
      <div class="day"><b>14</b><span>金</span></div>
      <div class="day active"><b>15</b><span>土</span>
        <div class="slots"><span>11:30</span><span>12:00</span><span>12:30</span><span>13:00</span><span>13:30</span></div>
      </div>
    </div>
    <p class="cal-foot en">Powered by SlotBook</p>
  </div>
</section>

<div class="band">エンジニア転職するならソラノ転職。</div>

<footer class="site-footer">
  <div class="brand">ソラノ転職EXPO</div>
  <p>運営会社：株式会社ミルテック<br>〒150-0042 東京都渋谷区宇田川町 4-12 ミルテックビル 5F</p>
</footer>
<div class="copyright en">© Sorano Jobchange Expo. All rights reserved.</div>

</body>
</html>
```